Web Design For Metal Recycling Company

We are a scrap and recycling company dealing mainly in scrap metal base in Singapore. We deal in both domestic market and international market. Currently we are still unsure if we want to have a "lively" or "professional" company image so we will leave it to the designer to deem what is good.

We wish for a website to be able to "Retain" the interest of new visitor and at the same time able to give enough information for new and existing customer. We would also wish for design that will get the visitor to "Engage" us.

The attached is the logo for the company and we would want to incorporate that into the website. Either of the logo is fine.

```html
<!DOCTYPE html>
<html lang="en">
<head>
<meta charset="utf-8">
<title>Tan Hock Metals – Business Solutions</title>
<link href="https://fonts.googleapis.com/css2?family=Open+Sans:ital,wght@0,400;0,600;0,700;0,800;1,400&display=swap" rel="stylesheet">
<style>
:root{
  --red:#d63c3e;
  --red-dark:#b52d30;
  --navy:#2f3e50;
  --navy-dark:#243140;
  --ink:#333;
  --muted:#777;
  --band:#ececec;
  --light:#f6f6f6;
  --white:#fff;
  --card-line:#dcdcdc;
}
*{margin:0;padding:0;box-sizing:border-box}
html,body{width:1200px;height:1200px;overflow:hidden}
body{position:relative;background:var(--white);font-family:'Open Sans',sans-serif;color:var(--ink)}
.abs{position:absolute}

/* header */
.site-header{left:0;top:0;width:1200px;height:58px;background:var(--red)}
.brand{left:212px;top:0;height:58px;display:flex;align-items:center;gap:8px;color:var(--white);font-weight:700;font-size:15px;letter-spacing:.3px;white-space:nowrap}
.brand-mark{width:12px;height:12px;background:var(--white)}
.main-nav{left:415px;top:0;height:58px;display:flex}
.main-nav a{display:block;height:58px;line-height:58px;padding:0 20px;color:var(--white);font-size:11px;font-weight:700;text-decoration:none;letter-spacing:.3px}
.main-nav a.is-active{background:var(--red-dark);padding:0 21px}
.social{left:930px;top:22px;display:flex;gap:14px}
.social span{width:14px;height:14px;border-radius:50%;background:var(--white)}

/* hero */
.hero{left:0;top:58px;width:1200px;height:332px;background:
  radial-gradient(ellipse at 70% 30%,#e9a27a 0%,transparent 45%),
  radial-gradient(ellipse at 20% 70%,#c9683f 0%,transparent 50%),
  linear-gradient(120deg,#f3e7e0 0%,#c76b45 35%,#8f3a1f 60%,#d98c63 80%,#f1ddd2 100%)}
.hero-arrow{top:205px;width:30px;height:34px;background:var(--red);display:flex;align-items:center;justify-content:center}
.hero-arrow.prev{left:0}.hero-arrow.next{right:0}
.hero-caption-title{left:213px;top:244px;width:383px;height:36px;background:var(--red);color:var(--white);font-size:17px;line-height:36px;padding-left:20px}
.hero-caption-title b{font-weight:800}
.hero-caption-body{left:213px;top:280px;width:383px;height:70px;background:rgba(40,44,52,.88);color:#e6e6e6;font-size:11.5px;line-height:17px;padding:9px 20px}

/* features */
.features{left:0;top:390px;width:1200px;height:130px;background:var(--light)}
.feature{top:436px;display:flex;gap:12px;width:190px}
.feature svg{flex:none;margin-top:2px}
.feature h3{color:var(--red);font-size:14px;font-weight:400;margin-bottom:2px}
.feature p{font-size:10px;line-height:14px;color:var(--muted)}

/* band */
.band{left:0;top:520px;width:1200px;height:617px;background:var(--band)}
.section-bar{left:213px;width:787px;height:38px;background:var(--red);color:var(--white);font-size:16px;font-weight:800;line-height:38px;padding-left:22px;letter-spacing:.5px;border-left:6px solid var(--red-dark)}
.section-bar .bar-btn{position:absolute;right:12px;top:11px;width:16px;height:16px;background:var(--red-dark)}
.section-bar.navy{background:var(--navy);border-left-color:var(--navy-dark)}
.section-bar.navy .bar-btn{background:var(--navy-dark)}
.bar-arrows{position:absolute;right:10px;top:11px;display:flex;gap:4px}
.bar-arrows span{width:16px;height:16px;background:var(--red-dark)}

.col-title{top:618px;font-size:17px;font-weight:700;color:#222}
.who-text{left:213px;top:657px;width:250px;font-size:9.5px;line-height:14px;color:#444}
.why-list{left:485px;top:656px;list-style:none;font-size:9.5px;color:#444}
.why-list li{display:flex;align-items:center;gap:10px;height:18px}
.why-list li::before{content:"";width:6px;height:6px;background:var(--red);transform:rotate(45deg)}
.test-arrows{left:962px;top:622px;display:flex;gap:4px}
.test-arrows span{width:16px;height:16px;background:#c9ccd2}
.quote{left:752px;top:663px;width:248px;height:74px;background:var(--white);border:1px solid #ddd;padding:14px 18px;font-size:9.5px;line-height:15px;font-style:italic;color:var(--muted)}
.quote-author{left:785px;top:745px;font-size:10px;font-weight:700;color:var(--red)}

.team-card{top:869px;width:180px;height:226px;background:var(--white);border:1px solid var(--card-line)}
.team-photo{position:absolute;left:8px;top:8px;width:162px;height:160px;background:linear-gradient(180deg,#f2f2f2,#e4e4e4)}
.team-name{position:absolute;left:0;top:186px;width:100%;text-align:center;font-size:15px;color:#333}
.team-role{position:absolute;left:0;top:206px;width:100%;text-align:center;font-size:10px;color:var(--red)}
</style>
</head>
<body>

<header class="abs site-header"></header>
<div class="abs brand"><span class="brand-mark"></span>TAN HOCK METALS</div>
<nav class="abs main-nav">
  <a class="is-active">HOME</a><a>ABOUT</a><a>SERVICES</a><a>PRICES</a><a>CONTACT US</a>
</nav>
<div class="abs social"><span></span><span></span><span></span></div>

<section class="abs hero" role="img" aria-label="Close-up photograph of bundles of stripped copper wire"></section>
<div class="abs hero-arrow prev"><svg width="10" height="14"><path d="M8 1 2 7l6 6" fill="none" stroke="#fff" stroke-width="2"/></svg></div>
<div class="abs hero-arrow next"><svg width="10" height="14"><path d="M2 1l6 6-6 6" fill="none" stroke="#fff" stroke-width="2"/></svg></div>
<div class="abs hero-caption-title"><b>TAN HOCK</b> business solutions</div>
<div class="abs hero-caption-body">Tan Hock, your One Stop Solution to all your scrap ferrous, Non-Ferrous and other recyclable. With more than 30 years of experience in the industry, we know your needs.</div>

<section class="abs features"></section>
<div class="abs feature" style="left:221px">
  <svg width="22" height="18"><path d="M7 1h8l6 16H1z" fill="#3b4552"/><path d="M11 3v3M11 8v3M11 13v3" stroke="#fff" stroke-width="2"/></svg>
  <div><h3>New way of vision</h3><p>Our goal is high product quality and satisfying customer service.</p></div>
</div>
<div class="abs feature" style="left:421px">
  <svg width="22" height="18"><path d="M2 17C4 6 12 2 21 1c-1 9-6 14-15 13" fill="#3b4552"/><path d="M2 17 12 8" stroke="#fff" stroke-width="1.5"/></svg>
  <div><h3>Fresh ideas</h3><p>We have established strong relationships and trusts with our customers</p></div>
</div>
<div class="abs feature" style="left:621px">
  <svg width="22" height="18"><path d="M11 1 1 10h3v7h5v-5h4v5h5v-7h3z" fill="#3b4552"/></svg>
  <div><h3>Strong foundations</h3><p>First established in 1981, the company carries a long history of experience.</p></div>
</div>
<div class="abs feature" style="left:821px">
  <svg width="24" height="18"><circle cx="12" cy="5" r="4" fill="#3b4552"/><circle cx="4" cy="7" r="3" fill="#3b4552"/><circle cx="20" cy="7" r="3" fill="#3b4552"/><path d="M5 17c0-5 3-7 7-7s7 2 7 7zM0 16c0-3 2-5 4-5s3 1 3 1l-2 4zM24 16c0-3-2-5-4-5s-3 1-3 1l2 4z" fill="#3b4552"/></svg>
  <div><h3>Great support</h3><p>The company constantly grows and expands to meet industry demands.</p></div>
</div>

<section class="abs band"></section>

<div class="abs section-bar" style="top:547px">ABOUT US<span class="bar-btn"></span></div>

<h2 class="abs col-title" style="left:213px">Who We Are?</h2>
<p class="abs who-text">Tan Hock Hardware provides a one stop solution for procurement, recycling and trading of ferrous and non-ferrous scrap metal products for industries and individual. Tan Hock Hardware was first established in 1981 as "Tan Hock Lead Dealer" to provide the service of recycling of ferrous and non-ferrous scrap metal for the local market.</p>

<h2 class="abs col-title" style="left:482px">Why us?</h2>
<ul class="abs why-list">
  <li>Over 30 years of experience</li>
  <li>Reliable and trusted</li>
  <li>Experience both nationally and internationally</li>
  <li>Committed to future success</li>
  <li>One of the leading companies</li>
</ul>

<h2 class="abs col-title" style="left:752px">Testimonials</h2>
<div class="abs test-arrows"><span></span><span></span></div>
<blockquote class="abs quote">We did not consider to work with another company. Tan Hock was our top choice - our only choice. They provide quality work every time.</blockquote>
<div class="abs quote-author">Ray Tanner</div>

<div class="abs section-bar" style="top:796px">MEET THE TEAM<span class="bar-arrows"><span></span><span></span></span></div>

<article class="abs team-card" style="left:213px"><div class="team-photo" role="img" aria-label="Team member portrait placeholder"></div><div class="team-name">Marek Doval</div><div class="team-role">manager</div></article>
<article class="abs team-card" style="left:415px"><div class="team-photo" role="img" aria-label="Team member portrait placeholder"></div><div class="team-name">Lena Korvik</div><div class="team-role">client relations</div></article>
<article class="abs team-card" style="left:617px"><div class="team-photo" role="img" aria-label="Team member portrait placeholder"></div><div class="team-name">Pavel Renko</div><div class="team-role">sales</div></article>
<article class="abs team-card" style="left:820px"><div class="team-photo" role="img" aria-label="Team member portrait placeholder"></div><div class="team-name">Sara Velin</div><div class="team-role">office manager</div></article>

<div class="abs section-bar navy" style="top:1145px">SERVICES<span class="bar-btn"></span></div>

</body>
</html>
```